Cyber security company needs a flyer to promote its anti email phishing product

We need a flyer design for a new company based out of Cheltenham, England called 'Vaultmark'. We develop software that stops employees opening phishing emails. Our initial product is called 'Halcyon' - designed as a innovative new way to prevent phishing emails tricking employees from opening them. The solution is designed for Enterprise customers so it must have a corporate feel. Vaultmark is part of the latest BRTX accelerator so we are allowed to also use the BRTX and PLMV (UK) logo. The final design should communicate innovation and security. I like the design 10290027 by Orwen as a general look and feel

Need to provide copy for flyer and 5 days on reflection is to short a time period hence extension 10 days .

Target Market(s)

Enterprise sized customers. No particular vertical is being targeted

Requirements
Must have
• Somewhere the BRTX and PLMV logos. The blue shield logo is the Vaultmark one. The .eps .ai format are higher quality but will need the vaultmark text removed.
• Looking for a single fold design so a A4 is effectively an A5 with 4 sides.
• www.vaultmarkholdings.example
• Tel no. 44 (0) 207 555 0371
• info@vaultmarkholdings.example
Nice to have
• Must have a quality and corporate feel

```html
<!DOCTYPE html>
<html lang="en">
<head>
<meta charset="utf-8">
<title>Vaultmark Halcyon Brochure</title>
<link rel="stylesheet" href="https://fonts.googleapis.com/css2?family=Montserrat:ital,wght@0,500;0,700;0,800;1,700&family=Open+Sans:wght@400;600&display=swap">
<style>
  :root {
    --navy: #123b6b;
    --navy-deep: #0b2a52;
    --navy-mid: #1d4f86;
    --ink: #3a3f47;
    --paper: #ffffff;
    --paper-grey: #eef0f3;
    --backdrop: #e8e1dc;
    --photo-dark: #2a2f38;
    --photo-warm: #6b5a4c;
  }
  * { box-sizing: border-box; margin: 0; padding: 0; }
  html, body { width: 869px; height: 1200px; overflow: hidden; }
  body {
    background: var(--backdrop);
    font-family: "Open Sans", sans-serif;
    color: var(--ink);
    position: relative;
  }
  .spread {
    position: absolute;
    left: 54px;
    width: 760px;
    height: 537px;
    display: flex;
    box-shadow: 0 10px 28px rgba(60, 45, 35, 0.18);
  }
  .spread--outer { top: 42px; }
  .spread--inner { top: 621px; }
  .page {
    position: relative;
    width: 380px;
    height: 537px;
    overflow: hidden;
    background: var(--paper);
  }
  .page::after {
    content: "";
    position: absolute;
    top: 0; bottom: 0;
    width: 18px;
    pointer-events: none;
  }
  .page--left::after { right: 0; background: linear-gradient(to left, rgba(0,0,0,0.10), rgba(0,0,0,0)); }
  .page--right::after { left: 0; background: linear-gradient(to right, rgba(0,0,0,0.10), rgba(0,0,0,0)); }
  .page svg.art { position: absolute; inset: 0; }

  /* Back cover */
  .back-cover { background: linear-gradient(160deg, var(--navy-mid) 0%, var(--navy) 45%, var(--navy-deep) 100%); }
  .brand-badge {
    position: absolute;
    display: flex;
    align-items: center;
    justify-content: center;
    border-radius: 50%;
    background: var(--paper);
    font-family: "Montserrat", sans-serif;
    font-weight: 700;
    color: var(--navy);
  }
  .back-cover .brand-badge { left: 155px; top: 148px; width: 70px; height: 70px; font-size: 10px; }
  .contact-list {
    position: absolute;
    left: 0; right: 0; top: 292px;
    list-style: none;
    text-align: center;
    color: var(--paper);
    font-size: 11px;
    letter-spacing: 0.3px;
  }
  .contact-list li { margin-bottom: 18px; }
  .contact-list svg { display: block; margin: 0 auto 4px; }
  .partners {
    position: absolute;
    left: 0; right: 0; top: 478px;
    text-align: center;
    color: var(--paper);
    font-size: 8.5px;
    letter-spacing: 0.4px;
    opacity: 0.85;
  }
  .partners__row { display: flex; justify-content: center; gap: 12px; margin-top: 6px; }
  .partner-badge { width: 44px; height: 22px; border-radius: 4px; background: rgba(255,255,255,0.85); }

  /* Front cover */
  .front-cover { background: linear-gradient(180deg, var(--paper-grey), var(--paper) 60%); }
  .front-cover .brand-badge {
    left: 208px; top: 130px; width: 118px; height: 118px; font-size: 15px;
    border: 4px solid var(--paper);
    box-shadow: 0 0 0 2px var(--navy);
  }
  .cover-title {
    position: absolute;
    left: 40px; right: 20px; top: 300px;
    text-align: center;
    font-family: "Montserrat", sans-serif;
    color: var(--navy);
  }
  .cover-title__main { font-size: 29px; font-weight: 800; letter-spacing: 0.5px; line-height: 1.1; }
  .cover-title__sub {
    display: inline-block;
    font-size: 12px; font-weight: 500;
    color: var(--ink);
    border-top: 1px solid #9aa4b1;
    border-bottom: 1px solid #9aa4b1;
    padding: 3px 6px;
    margin: 4px 0 6px;
  }
  .cover-title__url {
    margin-top: 14px;
    font-family: "Open Sans", sans-serif;
    font-size: 9px;
    letter-spacing: 2px;
    color: var(--ink);
  }
  .cover-title__rule { width: 80px; height: 5px; background: var(--navy); margin: 5px auto 0; }

  /* Inner pages */
  .copy {
    position: absolute;
    left: 30px; right: 30px;
    font-size: 10.5px;
    line-height: 14px;
    text-align: justify;
  }
  .copy h2 {
    font-family: "Montserrat", sans-serif;
    font-style: italic;
    font-weight: 700;
    font-size: 12.5px;
    color: var(--navy);
    margin-bottom: 6px;
  }
  .copy p { margin-bottom: 9px; }
  .copy--left { top: 26px; }
  .copy--right { top: 40px; }
  .copy p.wrap-around { margin-left: 140px; }
</style>
</head>
<body>

<section class="spread spread--outer">
  <article class="page page--left back-cover">
    <svg class="art" width="380" height="537" viewBox="0 0 380 537">
      <rect x="200" y="0" width="60" height="40" fill="var(--paper)"/>
      <rect x="150" y="38" width="40" height="30" fill="var(--paper)"/>
      <rect x="214" y="58" width="38" height="32" fill="var(--paper)"/>
      <rect x="180" y="80" width="18" height="14" fill="var(--paper)"/>
      <rect x="158" y="100" width="9" height="8" fill="var(--paper)"/>
      <rect x="196" y="108" width="7" height="6" fill="var(--paper)"/>
      <circle cx="190" cy="183" r="80" fill="none" stroke="#ffffff" stroke-opacity="0.06" stroke-width="14"/>
      <circle cx="190" cy="183" r="120" fill="none" stroke="#ffffff" stroke-opacity="0.04" stroke-width="10"/>
    </svg>
    <div class="brand-badge">vaultmark</div>
    <ul class="contact-list">
      <li>
        <svg width="12" height="12" viewBox="0 0 12 12"><circle cx="6" cy="6" r="6" fill="#fff"/><path d="M4 3.2 L5 3 L5.6 4.6 L4.9 5.1 Q5.5 6.5 6.9 7.1 L7.4 6.4 L9 7 L8.8 8 Q6 8.6 3.9 5.8 Q3.4 4.4 4 3.2Z" fill="var(--navy)"/></svg>
        +44 (0) 207 555 0371
      </li>
      <li>
        <svg width="12" height="12" viewBox="0 0 12 12"><circle cx="6" cy="6" r="6" fill="#fff"/><rect x="3" y="4" width="6" height="4.2" fill="none" stroke="var(--navy)" stroke-width="0.9"/><path d="M3 4 L6 6.4 L9 4" fill="none" stroke="var(--navy)" stroke-width="0.9"/></svg>
        info@vaultmarkholdings.example
      </li>
      <li>
        <svg width="12" height="12" viewBox="0 0 12 12"><circle cx="6" cy="6" r="6" fill="#fff"/><circle cx="6" cy="6" r="3.2" fill="none" stroke="var(--navy)" stroke-width="0.9"/><path d="M2.8 6 H9.2 M6 2.8 V9.2" stroke="var(--navy)" stroke-width="0.8"/></svg>
        www.vaultmarkholdings.example
      </li>
      <li>
        <svg width="12" height="12" viewBox="0 0 12 12"><circle cx="6" cy="6" r="6" fill="#fff"/><path d="M6 9.5 Q3.4 6.4 3.6 4.8 A2.4 2.4 0 0 1 8.4 4.8 Q8.6 6.4 6 9.5Z" fill="var(--navy)"/><circle cx="6" cy="4.9" r="0.9" fill="#fff"/></svg>
        Cheltenham, England
      </li>
    </ul>
    <div class="partners">
      Part of the BRTX accelerator, supported by PLMV (UK)
      <div class="partners__row">
        <span class="partner-badge" role="img" aria-label="BRTX accelerator badge"></span>
        <span class="partner-badge" role="img" aria-label="PLMV badge"></span>
      </div>
    </div>
  </article>

  <article class="page page--right front-cover">
    <svg class="art" width="380" height="537" viewBox="0 0 380 537">
      <defs>
        <linearGradient id="officePhoto" x1="0" y1="0" x2="1" y2="1">
          <stop offset="0" stop-color="var(--photo-dark)"/>
          <stop offset="0.6" stop-color="var(--photo-warm)"/>
          <stop offset="1" stop-color="#8aa0b8"/>
        </linearGradient>
        <linearGradient id="networkGlow" x1="0" y1="0" x2="0" y2="1">
          <stop offset="0" stop-color="#dfe4ea"/>
          <stop offset="1" stop-color="#f4f6f8"/>
        </linearGradient>
      </defs>
      <rect x="255" y="0" width="125" height="260" fill="url(#networkGlow)" role="img" aria-label="Faint network pattern background"/>
      <path d="M0 0 H262 V210 Q180 238 150 232 Q80 222 40 150 Q20 110 0 98 Z" fill="url(#officePhoto)" role="img" aria-label="Photo of two colleagues reviewing data on a monitor in a dark office"/>
      <path d="M0 106 Q22 118 44 158 Q84 230 152 240 Q186 244 262 218" fill="none" stroke="var(--navy)" stroke-width="4"/>
      <circle cx="300" cy="190" r="95" fill="none" stroke="#c7cfd9" stroke-width="1"/>
    </svg>
    <div class="brand-badge">vaultmark</div>
    <div class="cover-title">
      <div class="cover-title__main">STOP PHISHING</div>
      <div class="cover-title__sub">Halcyon keeps your people one step ahead</div>
      <div class="cover-title__main">AT THE INBOX</div>
      <div class="cover-title__url">www.vaultmarkholdings.example</div>
      <div class="cover-title__rule"></div>
    </div>
  </article>
</section>

<section class="spread spread--inner">
  <article class="page page--left">
    <svg class="art" width="380" height="537" viewBox="0 0 380 537">
      <defs>
        <linearGradient id="teamPhoto" x1="0" y1="0" x2="1" y2="1">
          <stop offset="0" stop-color="#7d8da3"/>
          <stop offset="0.5" stop-color="#c9b39e"/>
          <stop offset="1" stop-color="#3a3434"/>
        </linearGradient>
      </defs>
      <circle cx="230" cy="320" r="95" fill="none" stroke="#e3e7ec" stroke-width="18"/>
      <path d="M70 258 Q110 248 150 236 Q190 250 222 258 V300 Q215 330 150 360 Z" fill="#7ea6d6"/>
      <path d="M0 300 Q40 270 90 262 L150 248 Q200 262 230 300 Q260 360 300 380 Q340 400 380 400 V537 H0 Z" fill="url(#teamPhoto)" role="img" aria-label="Photo of a team of five colleagues gathered around a laptop"/>
    </svg>
    <div class="copy copy--left">
      <h2>Phishing is a people problem</h2>
      <p>Most breaches still begin with a single email. A convincing link, a familiar name or an urgent request is all it takes for one employee to open the door to an attacker, and filters alone cannot catch every message that lands in a busy inbox.</p>
      <p>Vaultmark was founded in Cheltenham, England to close that gap. We build software that helps employees spot and avoid phishing emails before they are opened, protecting the whole enterprise.</p>
    </div>
  </article>

  <article class="page page--right">
    <svg class="art" width="380" height="537" viewBox="0 0 380 537">
      <circle cx="60" cy="230" r="70" fill="none" stroke="#eef1f4" stroke-width="16"/>
      <path d="M0 320 H30 A90 90 0 0 1 120 410 V440 A20 20 0 0 1 100 460 H0 Z" fill="var(--navy)"/>
    </svg>
    <div class="copy copy--right">
      <h2>Meet Halcyon by Vaultmark</h2>
      <p>Halcyon is an innovative new way to stop phishing emails from tricking employees. It works quietly alongside your existing mail platform, assessing each message and stepping in at the moment a risky email is about to be opened.</p>
      <p>Rather than relying on annual training alone, Halcyon guides people in real time, so good security habits are built into everyday work.</p>
      <p>Designed for enterprise customers in every sector, Halcyon scales across large workforces, offers clear reporting for security teams and is simple to roll out.</p>
      <p class="wrap-around">Vaultmark is proud to be part of the latest BRTX accelerator, working with PLMV (UK) to bring new thinking to email security and keep organisations safer from the threats that target their people.</p>
      <p class="wrap-around">Call +44 (0) 207 555 0371 or email info@vaultmarkholdings.example to arrange a demo.</p>
    </div>
  </article>
</section>

</body>
</html>
```